Calderon Lending. Website design for a mortgage company.

We need a simple, but classy and artistic website design. The website should contain a home page, about page, and information page. I would like the design for each page created and I can add the content.

Calderon Lending is a retail mortgage broker business specially crafted to provide simple, transparent, and comprehensive mortgage solutions. We understand the complexities of mortgage acquisition and have aligned with the best partners and resources to analyze the information and deliver precise, transparent, efficient, and reliable results.

Target Market(s)

We are targeting people ages 30-65 within the United States, both male and female. We are also targeting business owners and property investors specifically.

Industry/Entity Type

Mortgage Brokerage

Coding

Coded - Design and coding required

Number of Pages Required

5+ page

Font styles to use
Sans Serif
Script

Requirements
Must have
• The main purpose of this website is to provide clients with the necessary information to want to move forward with a loan transaction. The website will be informational to promote the company and showcase our purpose. The company purpose is to provide efficient and comprehensive service to clients, and to help them navigate the challenging mortgage world.

The website must mimic that of the major fortune 500 companies. It needs to be super clean, but very modern. The pictures should be of families with brown skin mostly.

The website needs to be mobile responsive. Each page needs to consist of large and responsive Hero Images. There will be background videos on the product and process pages of the website.

The website must have a semi-flat design.
The website must have a Hamburger Menu instead of a visible navigation menu.

Use the script font styles for the headlines and the sans serif for body text.

We need to have the following pages:
Home

Products

Process

About

Contact - I want a map of our office location and region. We are located in Bowie MD and our region consists of the following states: Florida, Texas, Virginia, Maryland, and Washington DC.

```html
<!DOCTYPE html>
<html lang="en">
<head>
<meta charset="utf-8">
<title>Calderon Lending</title>
<link href="https://fonts.googleapis.com/css2?family=Cabin:wght@400;500;600&family=Satisfy&family=Dancing+Script:wght@500&display=block" rel="stylesheet">
<style>
:root{
  --blue:#1546c8;
  --blue-dark:#0f3aa8;
  --navy:#0b1f5c;
  --ink:#1b1b1b;
  --text:#3a3a3a;
  --pale:#e4ebf7;
  --white:#ffffff;
}
*{margin:0;padding:0;box-sizing:border-box}
html,body{width:1200px;height:3177px;overflow:hidden}
body{position:relative;background:var(--white);font-family:'Cabin',sans-serif;color:var(--text)}
.abs{position:absolute}
.script{font-family:'Satisfy','Dancing Script',cursive;color:var(--blue);font-weight:400;line-height:1.2;white-space:nowrap}
.btn{position:absolute;display:flex;align-items:center;justify-content:center;border-radius:22px;font-family:'Cabin',sans-serif;font-weight:500;font-size:16px;letter-spacing:.2px}
.btn-solid{background:var(--blue);color:var(--white)}
.btn-outline{border:1.5px solid var(--blue);color:var(--blue);background:transparent}

/* header */
.site-header{left:0;top:0;width:1200px;height:101px;background:var(--white)}
.brand{left:144px;top:43px;font-size:30px;font-weight:600;color:var(--ink);letter-spacing:-.3px;line-height:1}
.brand-dot{left:144px;top:20px;width:14px;height:14px;background:var(--blue)}
.tagline{left:264px;top:76px;font-size:12px;color:var(--ink)}
.phone{left:816px;top:38px;font-size:23px;color:var(--ink);display:flex;align-items:center;gap:8px;font-weight:500}
.menu-btn{left:1006px;top:26px;width:50px;height:50px;border-radius:50%;background:var(--blue);display:flex;align-items:center;justify-content:center}

/* hero */
.hero{left:0;top:101px;width:1200px;height:513px;background:linear-gradient(180deg,#7fa0c4 0%,#8f8a7a 30%,#6f6050 48%,#4f7a2c 62%,#3d6b1f 100%)}
.hero-caption{left:354px;top:279px;width:493px;height:134px;background:rgba(40,40,40,.72)}
.hero-title{left:354px;top:287px;width:493px;text-align:center;color:var(--white);font-size:41px;font-weight:500;line-height:44px}
.hero-arrow{width:44px;height:44px;border-radius:50%;background:var(--blue);display:flex;align-items:center;justify-content:center}

/* welcome */
.welcome-title{left:144px;top:692px;width:470px;font-size:42px;overflow:visible}
.welcome-text{left:144px;top:770px;width:436px;font-size:16.5px;line-height:28.7px;color:var(--text)}
.welcome-photo{left:639px;top:699px;width:417px;height:335px;border-radius:3px;background:linear-gradient(135deg,#b9c4b8 0%,#7f8d86 45%,#5b4a40 75%,#2e2a28 100%)}

/* services */
.services{left:0;top:1122px;width:1200px;height:496px;background:var(--pale)}
.services-title{left:144px;top:1190px;font-size:44px}
.service-title{font-size:24px;font-weight:500;color:var(--blue)}
.service-text{width:290px;font-size:12.3px;line-height:22.2px;color:var(--ink)}

/* reviews */
.reviews-title{left:0;width:1200px;top:1680px;text-align:center;font-size:44px}
.review-card{left:144px;top:1753px;width:912px;height:319px;background:var(--pale)}
.reviewer-photo{left:228px;top:1737px;width:234px;height:335px;border-radius:110px 110px 0 0;background:linear-gradient(180deg,#6a4a33 0%,#d6a98b 22%,#9db6d3 40%,#8aa6c8 100%)}
.quote{left:545px;top:1799px;width:475px;font-size:18.5px;line-height:33.5px;color:var(--ink)}
.reviewer{left:545px;top:1950px;font-size:17px;font-weight:600;color:var(--ink)}
.dot{top:2005px;width:11px;height:11px;border-radius:50%;background:#8aa2cc}
.dot.active{background:#111}

/* blog */
.blog{left:0;top:2157px;width:1200px;height:586px;background:var(--pale)}
.blog-title{left:0;width:1200px;top:2228px;text-align:center;font-size:44px}
.blog-card{top:2296px;width:440px;height:368px}
.blog-card .shade{position:absolute;left:0;bottom:0;width:100%;height:140px;background:linear-gradient(180deg,rgba(0,0,0,0),rgba(0,0,0,.82))}
.blog-date{position:absolute;left:23px;top:274px;font-size:15.5px;font-weight:500;color:var(--white)}
.blog-head{position:absolute;left:23px;top:300px;width:400px;font-size:20.5px;line-height:26px;color:var(--white)}

/* contact */
.contact-title{left:0;width:1200px;top:2807px;text-align:center;font-size:44px}
.contact-text{left:140px;width:920px;top:2869px;text-align:center;font-size:19px;line-height:32px;color:var(--ink)}

/* footer */
.site-footer{left:0;top:3065px;width:1200px;height:112px;background:var(--navy)}
.footer-links{left:144px;top:3097px;font-size:11.5px;color:#8fa6e0;word-spacing:2px}
.copyright{left:144px;top:3129px;font-size:11.5px;color:#8fa6e0}
.social{top:3110px;width:20px;height:20px;border-radius:50%;border:2px solid #6f8fe0}
</style>
</head>
<body>

<header class="abs site-header">
  <div class="abs brand-dot"></div>
  <div class="abs brand">CALDERON LENDING</div>
  <div class="abs tagline">A retail mortgage broker</div>
  <div class="abs phone">
    <svg width="18" height="18" viewBox="0 0 24 24"><path fill="#1b1b1b" d="M6.6 10.8a15.1 15.1 0 0 0 6.6 6.6l2.2-2.2c.3-.3.7-.4 1-.2 1.1.4 2.3.6 3.6.6.6 0 1 .4 1 1V20c0 .6-.4 1-1 1A17 17 0 0 1 3 4c0-.6.4-1 1-1h3.5c.6 0 1 .4 1 1 0 1.3.2 2.5.6 3.6.1.3 0 .7-.2 1z"/></svg>
    654 321 7720
  </div>
  <div class="abs menu-btn">
    <svg width="20" height="16" viewBox="0 0 20 16"><rect y="0" width="20" height="3" rx="1.5" fill="#fff"/><rect y="6.5" width="20" height="3" rx="1.5" fill="#fff"/><rect y="13" width="20" height="3" rx="1.5" fill="#fff"/></svg>
  </div>
</header>

<section class="abs hero" role="img" aria-label="Large brick family home with a green lawn and trees"></section>
<div class="abs hero-caption"></div>
<h1 class="abs hero-title">Vestibulum condimentum risus posuere cursus</h1>
<a class="btn btn-solid" style="left:536px;top:394px;width:128px;height:42px">READ MORE</a>
<div class="abs hero-arrow" style="left:46px;top:336px"><svg width="14" height="20" viewBox="0 0 14 20"><path d="M11 2 3 10l8 8" stroke="#fff" stroke-width="3" fill="none"/></svg></div>
<div class="abs hero-arrow" style="left:1106px;top:336px"><svg width="14" height="20" viewBox="0 0 14 20"><path d="M3 2l8 8-8 8" stroke="#fff" stroke-width="3" fill="none"/></svg></div>

<div class="abs welcome-photo" role="img" aria-label="Father and young daughter washing hands at a kitchen sink"></div>
<h2 class="abs script welcome-title">Welcome to Calderon Lending</h2>
<p class="abs welcome-text">Calderon Lending is a retail mortgage broker business specially crafted to provide simple, transparent, and comprehensive mortgage solutions. We understand the complexities of mortgage acquisition and have aligned with the best partners and resources to analyze the information and deliver precise, transparent, efficient, and reliable results.</p>
<a class="btn btn-solid" style="left:144px;top:985px;width:128px;height:44px">READ MORE</a>

<section class="abs services"></section>
<h2 class="abs script services-title">Our Services</h2>

<svg class="abs" style="left:144px;top:1278px" width="80" height="80" viewBox="0 0 80 80" fill="none" stroke="#1546c8" stroke-width="2.5"><path d="M4 56h14v20H4zM18 60h18l10-6c4-2 8 2 5 5L36 70H18"/><rect x="22" y="24" width="18" height="22" rx="4"/><text x="27" y="41" fill="#1546c8" stroke="none" font-size="14" font-family="Cabin">$</text><path d="M42 46V20h14v26M58 46V34l10-8 10 8v12"/></svg>
<svg class="abs" style="left:458px;top:1278px" width="80" height="80" viewBox="0 0 80 80" fill="none" stroke="#1546c8" stroke-width="2.5"><rect x="4" y="2" width="50" height="74" rx="2"/><path d="M12 14h34M12 22h34M12 30h26M12 38h20"/><circle cx="18" cy="58" r="8"/><path d="M14 58l3 3 6-6M30 62c6-8 10 6 16-4M72 12 48 50l-4 8 7-5 24-38z"/></svg>
<svg class="abs" style="left:772px;top:1278px" width="84" height="80" viewBox="0 0 84 80" fill="none" stroke="#1546c8" stroke-width="2.5"><path d="M4 2h34l10 10v66H4z"/><path d="M12 20h24M12 28h24M12 36h24M12 44h24M12 52h20"/><rect x="36" y="38" width="44" height="40" rx="3"/><rect x="42" y="44" width="32" height="8"/><path d="M44 58h6M54 58h6M64 58h6M44 66h6M54 66h6M64 66h6M44 72h6M54 72h6M64 72h6"/></svg>

<h3 class="abs service-title" style="left:144px;top:1374px">Pellentesque</h3>
<h3 class="abs service-title" style="left:458px;top:1374px">Nulla facilisi</h3>
<h3 class="abs service-title" style="left:772px;top:1374px">Etiam mattis</h3>
<p class="abs service-text" style="left:144px;top:1412px">Vivamus lacus justo, ultrices nec erat euismod iaculis mauris. Vivamus eleifend vitae nulla vel malesuada. In ac malesuada lacus, et consectetur ante.</p>
<p class="abs service-text" style="left:458px;top:1412px">Vivamus lacus justo, ultrices nec erat euismod iaculis mauris. Vivamus eleifend vitae nulla vel malesuada. In ac malesuada lacus, et consectetur ante.</p>
<p class="abs service-text" style="left:772px;top:1412px">Vivamus lacus justo, ultrices nec erat euismod iaculis mauris. Vivamus eleifend vitae nulla vel malesuada. In ac malesuada lacus, et consectetur ante.</p>
<a class="btn btn-outline" style="left:144px;top:1496px;width:128px;height:44px">READ MORE</a>
<a class="btn btn-outline" style="left:458px;top:1496px;width:128px;height:44px">READ MORE</a>
<a class="btn btn-outline" style="left:772px;top:1496px;width:128px;height:44px">READ MORE</a>

<h2 class="abs script reviews-title">Reviews</h2>
<div class="abs review-card"></div>
<div class="abs reviewer-photo" role="img" aria-label="Smiling man in a light blue shirt with arms crossed"></div>
<p class="abs quote">“ Nunc eu ligula sed quam pulvinar maximus in vitae eros. Proin porta fermentum vel porttitor turpis venenatis luctus. Vivamus volutpat eu sapien quis tempus. Aenean feugiat viverra lorem ac sagittis.&nbsp; ”</p>
<div class="abs reviewer">MARCUS REED, CITY</div>
<span class="abs dot active" style="left:545px"></span>
<span class="abs dot" style="left:577px"></span>
<span class="abs dot" style="left:609px"></span>
<span class="abs dot" style="left:641px"></span>

<section class="abs blog"></section>
<h2 class="abs script blog-title">Blog</h2>
<svg class="abs" style="left:56px;top:2468px" width="16" height="26" viewBox="0 0 16 26"><path d="M13 2 3 13l10 11" stroke="#5a6c8e" stroke-width="3" fill="none"/></svg>
<svg class="abs" style="left:1124px;top:2468px" width="16" height="26" viewBox="0 0 16 26"><path d="M3 2l10 11L3 24" stroke="#5a6c8e" stroke-width="3" fill="none"/></svg>
<article class="abs blog-card" style="left:144px;background:linear-gradient(160deg,#4a4f4a 0%,#6b5a52 40%,#3a4240 70%,#2a2e2c 100%)" role="img" aria-label="Aerial view of a suburban neighbourhood">
  <div class="shade"></div>
  <div class="blog-date">23 MAY, 2020</div>
  <div class="blog-head">Aliquam dignissim elit nec mauris porta, vitae pretium risus</div>
</article>
<article class="abs blog-card" style="left:615px;background:linear-gradient(180deg,#1f54c4 0%,#1e3f8c 40%,#5a4a38 70%,#1a1a1a 100%)" role="img" aria-label="Modern house lit up at dusk">
  <div class="shade"></div>
  <div class="blog-date">23 MAY, 2020</div>
  <div class="blog-head">Pellentesque vehicula nulla molestie lectus fermentum, id egestas velit</div>
</article>

<h2 class="abs script contact-title">Contact Us</h2>
<p class="abs contact-text">Cras sed augue tortor. Suspendisse elit ligula, iaculis dignissim justo eu, vestibulum venenatis elit. Sed egestas, nisl id cursus ultricies, turpis orci rhoncus odio, id tristique odio ex in lacus.</p>
<a class="btn btn-solid" style="left:536px;top:2943px;width:128px;height:44px">EMAIL US</a>

<footer class="abs site-footer"></footer>
<div class="abs footer-links">Home &nbsp;|&nbsp; About Us &nbsp;|&nbsp; Services &nbsp;|&nbsp; Reviews &nbsp;|&nbsp; Blog &nbsp;|&nbsp; Contact Us</div>
<div class="abs copyright">Copyright &copy; 2020 &nbsp;Calderon Lending. &nbsp;All rights reserved.</div>
<span class="abs social" style="left:990px" aria-label="Social link"></span>
<span class="abs social" style="left:1034px" aria-label="Social link"></span>

</body>
</html>
```